Visitenkarte für Ergotherapiepraxis
Zielgruppe
Wir arbeiten mit Kindern und Erwachsene jeden Alters.
Diese Personen kommen mit Beeinträchtigungen (körperlich, seelisch, schulisch) im täglichen Leben zu uns. Wir unterstützen unsere Patienten die Beeinträchtigungen zu verringern oder zu kompensieren und so den Alltag besser bewältigen zu können.
Aufgabenstellung
Ein Design was Kinder und Erwachsene anspricht, aber nicht zu verspielt wirkt. Es soll vertrauenserweckend sein. Eventuell sollte die Visitenkarte ein "aufgehendes oder erblühendes oder aufsteigendes" Element enthalten (=zu Beginn war die Beeinträchtigung dann steigt die Lebensqualität als Folge der Behandlung)
Daten vorn:
Ergotherapiepraxis

```html
<!DOCTYPE html>
<html lang="de">
<head>
<meta charset="utf-8">
<title>Visitenkarte Ergotherapiepraxis</title>
<link rel="stylesheet" href="https://fonts.googleapis.com/css2?family=Open+Sans:wght@400;600;700&display=swap">
<style>
  :root {
    --teal: #00a595;
    --teal-dark: #008c7e;
    --grey-text: #4d4d4f;
    --grey-light: #6d6e70;
    --white: #ffffff;
    --backdrop: #dfe2e6;
  }
  * { margin: 0; padding: 0; box-sizing: border-box; }
  html, body {
    width: 1200px; height: 675px; overflow: hidden;
    background: var(--backdrop);
    font-family: "Open Sans", sans-serif;
  }
  .card {
    position: absolute; left: 150px; top: 47px;
    width: 900px; height: 580px;
    background: var(--white); overflow: hidden;
    box-shadow: 0 6px 24px rgba(0,0,0,.18);
  }
  .band { position: absolute; left: 0; width: 100%; background: var(--teal); }
  .band--top { top: 0; height: 62px; }
  .band--middle { top: 268px; height: 150px; }
  .band--bottom { top: 530px; height: 50px; }
  .logo-disc {
    position: absolute; left: 40px; top: 44px;
    width: 400px; height: 400px; border-radius: 50%;
    background: var(--white);
    display: flex; align-items: center; justify-content: center; gap: 14px;
  }
  .logo-disc__dot { width: 34px; height: 34px; border-radius: 50%; background: var(--teal); }
  .logo-disc__name { font-weight: 700; font-size: 34px; color: var(--teal); }
  .contact {
    position: absolute; left: 470px; top: 118px;
  }
  .contact__practice { font-weight: 700; font-size: 44px; color: var(--teal); line-height: 1.05; letter-spacing: -0.5px; }
  .contact__name { font-weight: 600; font-size: 38px; color: var(--grey-text); line-height: 1.1; }
  .contact__phone { font-weight: 400; font-size: 24px; color: var(--grey-light); margin-top: 6px; margin-left: 30px; }
  .address {
    position: absolute; left: 0; top: 418px; width: 100%; height: 112px;
    display: flex; align-items: center; justify-content: center; gap: 34px;
    font-size: 30px; font-weight: 400; color: var(--grey-text);
  }
  .address__divider { color: var(--grey-light); }
</style>
</head>
<body>
  <article class="card">
    <div class="band band--top"></div>
    <div class="band band--middle"></div>
    <div class="band band--bottom"></div>

    <div class="logo-disc">
      <span class="logo-disc__dot"></span>
      <span class="logo-disc__name">Ergopraxis Sturm</span>
    </div>

    <div class="contact">
      <p class="contact__practice">Ergotherapiepraxis</p>
      <p class="contact__name">Marlene Sturm</p>
      <p class="contact__phone">Tel. 033840 / 51724</p>
    </div>

    <p class="address">
      <span class="address__street">Am Lindenweg 12</span>
      <span class="address__divider">|</span>
      <span class="address__town">15837 Fernwalde, OT Birkholz</span>
    </p>
  </article>
</body>
</html>
```